Documentary Film Poster Design Project

I'm looking to hire someone to design a 11 x 17 poster for my documentary film, "Beyond the Drift," which is about plastic pollution in the atlantic ocean. The film is accepted into four film international film festivals (so far), so your design would have wide exposure.

www.beyondthedrift-film.example

I'm looking for something fairly straightforward, that incorporates some textual information for the film, along with (maybe) existing photographs and your amazing design skills. Please do not include images of PET soda/water bottles. The film has a science advisory board which is very specific about using the correct representation of oceanic plastic pollution.

I'd like to own the rights to this poster and have the poster be scalable to printed postcards and DVD packaging.
Updates

Target Market(s)

This poster will be used at film festivals to promote the film and attract viewers to attend. It should be bold and striking, making people take notice of it and say, "that's a cool poster, I'd like to see that film about plastic pollution. It also looks like it was filmed on a ship. cool."

Industry/Entity Type

Plastic

Requirements
Must have
• The poster must have the following textual information in it. Basically as you see in any movie poster. I'm looking for interesting typography in this poster, especially with the title. In someway, I think it would be nice to play with the idea of little pieces of plastic in the visual look of the title, but that's for you to decide. I've also attached images of the motion-graphics in the film, but do not feel like you have to use these.

Beyond the Drift

A documentary about plastic pollution

A 417reels production A film by Marcus Hadley
cinematography by Marcus Hadley and Owen Drummark edited by Marcus Hadley written by Marcus Hadley and Petra Hadley produced and directed by Marcus Hadley

www.beyondthedrift-film.example
www.driftsocial.example/BeyondTheDrift

```html
<!DOCTYPE html>
<html lang="en">
<head>
<meta charset="utf-8">
<title>Beyond the Drift — Poster</title>
<link rel="stylesheet" href="https://fonts.googleapis.com/css2?family=Anton&family=Roboto+Condensed:wght@400;700&display=swap">
<style>
  :root {
    --navy: #1e2a5e;
    --navy-deep: #16204a;
    --sea-light: #3a4f8c;
    --deck-dark: #6f6a62;
    --deck-light: #c8c1b3;
    --rope-light: #d9d2c4;
    --cable-dark: #15151a;
    --white: #ffffff;
  }
  html, body {
    margin: 0;
    padding: 0;
    width: 776px;
    height: 1200px;
    overflow: hidden;
    background: var(--navy-deep);
  }
  .poster {
    position: relative;
    width: 776px;
    height: 1200px;
    overflow: hidden;
    font-family: "Roboto Condensed", "Arial Narrow", sans-serif;
    color: var(--white);
  }
  .sea-photo {
    position: absolute;
    left: 0; top: 0;
    width: 776px; height: 990px;
    background: radial-gradient(ellipse at 30% 60%, var(--sea-light), var(--navy) 55%, var(--navy-deep));
  }
  .plastic-field {
    position: absolute;
    left: 0; top: 0;
    width: 776px; height: 975px;
    background:
      linear-gradient(160deg, rgba(242,30,230,.85) 0%, rgba(126,240,238,.8) 22%, rgba(245,106,18,.85) 40%, rgba(46,224,31,.8) 58%, rgba(140,44,240,.85) 76%, rgba(245,67,122,.85) 100%);
  }
  .deck-photo {
    position: absolute;
    left: 0; top: 975px;
    width: 776px; height: 225px;
    background: linear-gradient(180deg, var(--deck-dark) 0%, #a39b8d 30%, var(--deck-light) 60%, #b3ab9c 100%);
  }
  .title-art, .rigging {
    position: absolute;
    left: 0; top: 0;
  }
  .title-word {
    font-family: "Anton", "Impact", sans-serif;
    fill: var(--navy);
  }
  .tagline {
    position: absolute;
    right: 36px;
    top: 1056px;
    margin: 0;
    font-weight: 700;
    font-size: 37px;
    line-height: 1;
    white-space: nowrap;
    text-align: right;
  }
  .credits {
    position: absolute;
    left: 60px;
    top: 1105px;
    margin: 0;
    font-size: 10.5px;
    line-height: 15px;
    white-space: nowrap;
  }
  .credits span { display: block; }
  .links {
    position: absolute;
    right: 16px;
    top: 1115px;
    margin: 0;
    font-size: 10.5px;
    line-height: 18px;
    text-align: right;
  }
  .links span { display: block; }
</style>
</head>
<body>
<main class="poster">
  <div class="sea-photo" role="img" aria-label="Photograph of dark open ocean water seen from a ship"></div>
  <div class="plastic-field" role="img" aria-label="Mosaic of bright plastic fragments in magenta, cyan, orange, green, yellow and violet surrounding the title"></div>
  <div class="deck-photo" role="img" aria-label="Photograph of a ship's deck and cabin roof"></div>

  <svg class="title-art" width="776" height="975" viewBox="0 0 776 975" aria-label="Beyond the Drift">
    <text class="title-word" x="150" y="300" font-size="330" textLength="490" lengthAdjust="spacingAndGlyphs">BEYOND</text>
    <text class="title-word" x="150" y="600" font-size="340" textLength="490" lengthAdjust="spacingAndGlyphs">THE</text>
    <text class="title-word" x="150" y="900" font-size="340" textLength="490" lengthAdjust="spacingAndGlyphs">DRIFT</text>
  </svg>

  <svg class="rigging" width="776" height="1200" viewBox="0 0 776 1200" aria-hidden="true">
    <line x1="0" y1="680" x2="776" y2="215" stroke="var(--rope-light)" stroke-width="6"/>
    <line x1="0" y1="815" x2="776" y2="990" stroke="var(--cable-dark)" stroke-width="4"/>
    <line x1="0" y1="905" x2="776" y2="960" stroke="var(--cable-dark)" stroke-width="2"/>
    <line x1="0" y1="985" x2="776" y2="975" stroke="#e6e1d6" stroke-width="3"/>
    <line x1="360" y1="1200" x2="776" y2="1030" stroke="var(--cable-dark)" stroke-width="2"/>
  </svg>

  <h2 class="tagline">A documentary about plastic pollution</h2>

  <p class="credits">
    <span>A 417reels production A film by Marcus Hadley. Edited by Marcus Hadley.</span>
    <span>Cinematography by Marcus Hadley and Owen Drummark. written by Marcus Hadley</span>
    <span>and Petra Hadley produced and directed by Marcus Hadley.</span>
  </p>

  <p class="links">
    <span>www.beyondthedrift-film.example</span>
    <span>www.driftsocial.example/BeyondTheDrift</span>
  </p>
</main>
</body>
</html>
```